Lanternway Journeys Business Card Design for Home Based Travel Agency

We already have a logo and I would like to see about getting a Business Card Design. The font on the logo can be changed. We are a home based travel agency and sell cruises and tour packages, etc. I would like the following information put into the design Name of Company and Tag Line from the logo. I would also like the email info@lanternwayjourneys.example Phone 360-728-3415. Website www.lanternwayjourneys.example. My name Neil Harper Travel Consultant and my wife's Name Marcy Harper. I would like you to use your imagination as nothing is off limites. Impress Me!

Target Market(s)

Baby Boomers

Industry/Entity Type

Travel Agent

Contact Information for Business Card

See above

Font styles to use
Serif
Sans Serif

Colors

Designer to choose colors to be used in the design.

Requirements
Must have
• Play with different fonts and needs to be easily readable, i.e. not too small of print.
Nice to have
• Use your imagination

```html
<!DOCTYPE html>
<html lang="en">
<head>
<meta charset="utf-8">
<title>Lanternway Journeys – Business Card</title>
<link rel="stylesheet" href="https://fonts.googleapis.com/css2?family=Josefin+Sans:wght@300&family=Questrial&family=Roboto+Condensed:wght@400&display=swap">
<style>
  :root {
    --backdrop: #e8e3dc;
    --card-dark: #000000;
    --card-light: #ffffff;
    --ink: #111111;
    --paper-text: #ffffff;
    --accent: #f4a42c;
    --icon-ink: #4a2374;
  }
  * { box-sizing: border-box; margin: 0; padding: 0; }
  html, body { width: 1200px; height: 1200px; overflow: hidden; }
  body { background: var(--backdrop); position: relative; }

  .card {
    position: absolute;
    left: 238px;
    width: 742px;
    height: 412px;
    box-shadow: 0 10px 26px rgba(0,0,0,.22);
  }
  .card--front { top: 142px; background: var(--card-dark); }
  .card--back  { top: 622px; background: var(--card-light); }

  .brand { position: absolute; text-align: center; font-family: "Josefin Sans", sans-serif; font-weight: 300; }
  .brand__mark { display: block; margin: 0 auto 14px; width: 34px; height: 34px; background: var(--accent); }
  .brand__name { display: block; letter-spacing: .14em; text-transform: uppercase; line-height: 1.15; }
  .brand__tagline { display: block; font-family: "Questrial", sans-serif; margin-top: 6px; }

  .card--front .brand { left: 0; right: 0; top: 178px; color: var(--paper-text); }
  .card--front .brand__name { font-size: 30px; }
  .card--front .brand__tagline { font-size: 12px; color: #cfcfcf; }

  .front-rule { position: absolute; top: 369px; left: 44px; right: 44px; height: 10px; display: flex; align-items: center; gap: 8px; }
  .front-rule__dots { width: 26px; height: 4px; background-image: radial-gradient(circle, #fff 1.6px, transparent 1.8px); background-size: 6px 4px; }
  .front-rule__bar { flex: 1; height: 4px; background: var(--paper-text); }

  .card--back .brand { left: 40px; width: 222px; top: 150px; color: var(--ink); }
  .card--back .brand__name { font-size: 23px; }
  .card--back .brand__tagline { font-size: 10px; color: #333; }
  .back-divider { position: absolute; left: 290px; top: 48px; bottom: 48px; width: 3px; background: linear-gradient(to bottom, transparent, rgba(0,0,0,.35) 30%, rgba(0,0,0,.35) 70%, transparent); }

  .people { position: absolute; left: 320px; top: 52px; font-family: "Questrial", sans-serif; color: var(--ink); }
  .people__name { font-size: 23px; line-height: 27px; letter-spacing: .02em; }
  .people__role { font-size: 16px; letter-spacing: .06em; margin-top: 2px; padding-top: 2px; border-top: 2px solid var(--ink); width: 194px; }

  .contacts { position: absolute; left: 318px; top: 148px; list-style: none; }
  .contact { display: flex; align-items: center; height: 56px; margin-bottom: 17px; font-family: "Roboto Condensed", sans-serif; font-size: 24px; color: var(--ink); }
  .contact:nth-child(2) { margin-bottom: 24px; }
  .contact__icon { width: 50px; height: 56px; margin-right: 16px; flex: none; }
</style>
</head>
<body>

<section class="card card--front" aria-label="Card front">
  <div class="brand">
    <span class="brand__mark"></span>
    <span class="brand__name">Lanternway Journeys</span>
    <span class="brand__tagline">Every Journey Leaves a Light to Follow</span>
  </div>
  <div class="front-rule">
    <span class="front-rule__dots"></span>
    <span class="front-rule__bar"></span>
    <span class="front-rule__dots"></span>
  </div>
</section>

<section class="card card--back" aria-label="Card back">
  <div class="brand">
    <span class="brand__mark"></span>
    <span class="brand__name">Lanternway Journeys</span>
    <span class="brand__tagline">Every Journey Leaves a Light to Follow</span>
  </div>
  <div class="back-divider"></div>

  <div class="people">
    <p class="people__name">Neil Harper</p>
    <p class="people__name">Marcy Harper</p>
    <p class="people__role">Travel Consultant</p>
  </div>

  <ul class="contacts">
    <li class="contact">
      <svg class="contact__icon" viewBox="0 0 50 56" aria-hidden="true">
        <polygon points="25,1 49,14 49,42 25,55 1,42 1,14" fill="var(--accent)"/>
        <path d="M18 16c2-1 4 0 5 2l2 4c1 2 0 3-1 4l-2 1c1 3 3 6 6 8l1-2c1-1 3-2 4-1l4 2c2 1 2 3 1 5-2 3-5 3-8 2-6-3-11-9-13-15-1-4 0-8 1-10z" fill="var(--icon-ink)"/>
      </svg>
      <span>(360) 728 3415</span>
    </li>
    <li class="contact">
      <svg class="contact__icon" viewBox="0 0 50 56" aria-hidden="true">
        <polygon points="25,1 49,14 49,42 25,55 1,42 1,14" fill="var(--accent)"/>
        <rect x="12" y="19" width="26" height="18" rx="2" fill="none" stroke="var(--icon-ink)" stroke-width="3"/>
        <path d="M13 21l12 9 12-9M13 35l8-7M37 35l-8-7" fill="none" stroke="var(--icon-ink)" stroke-width="2.5"/>
      </svg>
      <span>info@lanternwayjourneys.example</span>
    </li>
    <li class="contact">
      <svg class="contact__icon" viewBox="0 0 50 56" aria-hidden="true">
        <polygon points="25,1 49,14 49,42 25,55 1,42 1,14" fill="var(--accent)"/>
        <g fill="none" stroke="var(--icon-ink)" stroke-width="3.2" stroke-linecap="round">
          <rect x="12" y="26" width="16" height="9" rx="4.5" transform="rotate(-45 20 30.5)"/>
          <rect x="22" y="21" width="16" height="9" rx="4.5" transform="rotate(-45 30 25.5)"/>
        </g>
      </svg>
      <span>www.lanternwayjourneys.example</span>
    </li>
  </ul>
</section>

</body>
</html>
```